Roofing & Siding door hanger flyer

-Looking to make door hanger flyer for Pellmont Roofing & Siding
-4.5" wide x 11" tall
-2 sided full colour
-We have started a new website (the content is changing) I have attached photos.
-About us:
-25 year labour warranty's available
-32 years in Calgary
-QCR A+ Member
-NWTG (Prairie Joint Shingle Guild) (logo attached)
-KOV Summit Select (logo attached)
-Owen Brisket (logo attached)
-Slogan "Raised On Care, Proven Through Seasons" 32 years in Calgary
-Sale
-Page 1 & 2 design ideas
We are in your area, contact us today for your Exclusive limited time offer! *discounts apply exclusively to new agreements only
Updates
-Please keep simple, clean & bright
-I really like the bright blue from our new logo (new logo uploaded)
-We specialize in Roofing -Siding-Gutters & full Exterior Renos (like the competitor example uploaded)
-This is the NEW website we are currently working on (not finished) https://mockview.example-draftpad.net/view/1a2b3c4d-5e6f-4a7b-8c9d-0e1f2a3b4c5d-7k2m/?fullscreen
-This is our OLD website https://pellmontshingleworks.com
-For the sale "We are in your area, contact us today for your Exclusive limited time offer" *discounts apply exclusively to new agreements only
-Free Estimates
-our phone# is 403-555-0148
-our website is pellmontshingleworks.com
-keep simple, clean, bright use the "new logo" uploaded. Check out the competitor example uploaded file
-We are in your area, Contact us today for your Exclusive limited time offer! *discounts apply to new agreements only
-FREE ESTIMATES
-Specialized in Roofing /Siding /Gutters Full Exterior Reno's
-We are currently working on a NEW website https://mockview.example-draftpad.net/view/1a2b3c4d-5e6f-4a7b-8c9d-0e1f2a3b4c5d-7k2m/?fullscreen
-Our OLD website https://pellmontshingleworks.com/
-Post old site address on flyer pellmontshingleworks.com
-Phone # 403-555-0148
Target Market(s)
40-55
Industry/Entity Type
Roofing Siding & full Exterior Reno's
Look and feel

```html
<!DOCTYPE html>
<html lang="en">
<head>
<meta charset="utf-8">
<title>Pellmont Roofing &amp; Siding – Door Hanger</title>
<link href="https://fonts.googleapis.com/css2?family=Anton&family=Oswald:wght@600;700&family=PT+Sans:wght@400;700&family=Poppins:wght@500;600&display=swap" rel="stylesheet">
<style>
  :root{
    --stage:#a0a2a1;
    --blue:#1a86ef;
    --blue-deep:#0f6fd6;
    --dark:#2a2a2a;
    --ink:#222426;
    --paper:#ffffff;
    --mist:#e8e9ea;
    --hole:#c6c7c8;
    --rule:#555;
    --warranty-grey:#7d7e80;
  }
  *{box-sizing:border-box;margin:0;padding:0}
  html,body{width:1200px;height:1200px;overflow:hidden}
  body{background:var(--stage);position:relative;font-family:"PT Sans",sans-serif}

  .hanger{position:absolute;top:121px;width:392px;height:957px;overflow:hidden;background:var(--mist)}
  .hanger--front{left:182px}
  .hanger--back{left:626px}
  .abs{position:absolute}

  /* hang hole */
  .hang-slot{left:0;top:112px;width:141px;height:17px;background:var(--hole)}
  .hang-hole{left:140px;top:64px;width:112px;height:112px;border-radius:50%;background:var(--hole)}

  /* photo placeholders */
  .photo-roof{left:0;top:150px;width:392px;height:500px;
    background:linear-gradient(180deg,#e3e6ea 0%,#b9c0c8 18%,#4a5058 34%,#2f343b 55%,#6b4a33 78%,#a0744d 100%)}
  .photo-home{left:0;top:0;width:392px;height:432px;
    background:linear-gradient(180deg,#3d86d6 0%,#8fb4dc 22%,#bfc2c6 40%,#d6d7d8 58%,#9aa09e 72%,#5f8a3a 84%,#4c7a2c 100%)}
  .thumb{width:92px;height:62px}
  .thumb--roofing{background:linear-gradient(180deg,#3e86d4 0%,#6a7078 55%,#e6e6e6 100%)}
  .thumb--siding{background:linear-gradient(180deg,#8ab7e6 0%,#4b5866 45%,#3a4652 100%)}
  .thumb--cladding{background:linear-gradient(135deg,#4b5158 0%,#9aa1a8 55%,#cfd3d6 100%)}
  .thumb--soffit{background:linear-gradient(90deg,#7fb3e8 0%,#cfe2f4 60%,#8aa07a 100%)}

  /* logo lockup */
  .logo-box{background:var(--paper);display:flex;align-items:center;justify-content:center;gap:6px}
  .logo-box--front{left:231px;top:0;width:161px;height:99px}
  .logo-box--back{left:133px;top:697px;width:125px;height:78px}
  .logo-mark{width:10px;height:10px;background:var(--blue);flex:none}
  .logo-name{font-family:"Poppins",sans-serif;font-weight:600;color:var(--ink);line-height:1.15;text-align:center;letter-spacing:.5px}
  .logo-box--front .logo-name{font-size:12px}
  .logo-box--back .logo-name{font-size:9.5px}

  /* headline */
  .headline{left:37px;top:224px;font-family:"Anton",sans-serif;font-weight:400;font-size:52px;line-height:63px;color:#fff;text-transform:uppercase;letter-spacing:0;white-space:nowrap}
  .headline .line{display:block}
  .headline .accent{color:var(--blue)}

  .years-badge{left:184px;top:450px;width:140px;height:140px}

  /* bottom band */
  .footer-wave{left:0;width:392px}
  .about-title{left:0;top:606px;width:392px;text-align:center;color:#fff;font-weight:700;font-size:14px;letter-spacing:1px}
  .about-copy{left:44px;top:626px;width:304px;text-align:center;color:#fff;font-size:10px;line-height:13.4px}

  .warranty{left:57px;top:703px;width:286px;height:72px;background:var(--paper)}
  .warranty-years{left:9px;top:7px;width:132px;height:45px}
  .warranty-label{left:134px;top:7px;width:143px;height:45px}
  .warranty-available{left:0;top:52px;width:286px;text-align:center;font-family:"Oswald",sans-serif;font-weight:700;font-size:13px;letter-spacing:8px;color:var(--ink)}

  .offer{left:0;width:392px;text-align:center;color:#fff;font-family:"Poppins",sans-serif;font-weight:500;font-size:9.6px}
  .phone{left:0;width:392px;display:flex;align-items:center;justify-content:center;gap:10px;color:#fff;font-family:"Poppins",sans-serif;font-weight:600;font-size:27px;letter-spacing:.5px}
  .phone-icon{width:28px;height:28px;background:var(--blue);border-radius:6px;display:flex;align-items:center;justify-content:center}
  .web{left:0;width:392px;text-align:center;color:#fff;font-family:"Poppins",sans-serif;font-weight:500;font-size:10.5px}
  .badges{left:53px;top:861px;width:285px;height:60px;background:var(--paper);display:flex;align-items:center;justify-content:space-around;padding:0 8px}
  .badge{background:#c9ccd0}
  .badge--wide{width:80px;height:24px;border-radius:2px}
  .badge--diamond{width:30px;height:30px;transform:rotate(45deg);background:#1f3f7a}
  .badge--tile{width:40px;height:40px;border-radius:3px;background:#a9acaf}
  .badge--plate{width:52px;height:22px;border-radius:3px;background:#1a7f8a}
  .badge--dot{width:16px;height:16px;border-radius:50%;background:#1a7f8a}
  .disclaimer{left:0;top:927px;width:392px;text-align:center;color:#fff;font-family:"Poppins",sans-serif;font-weight:500;font-size:9.8px}

  /* services */
  .services-pill{left:135px;top:370px;width:122px;height:22px;border-radius:11px;background:var(--blue);border:2px solid #fff;box-shadow:0 0 0 1px var(--blue-deep);color:#fff;font-family:"Poppins",sans-serif;font-weight:600;font-size:13px;display:flex;align-items:center;justify-content:center;letter-spacing:.5px}
  .service{width:180px;text-align:center;color:var(--ink)}
  .service-title{font-weight:700;font-size:12.5px;letter-spacing:1px;margin-bottom:3px}
  .service-copy{font-size:9.3px;line-height:12.7px}
  .divider-v{left:200px;top:396px;width:1px;height:282px;background:var(--rule)}
  .divider-h{left:51px;top:536px;width:298px;height:1px;background:var(--rule)}
</style>
</head>
<body>

<!-- FRONT -->
<section class="hanger hanger--front">
  <div class="abs photo-roof" role="img" aria-label="Photo of a roofer installing dark standing-seam metal roofing over cedar siding"></div>
  <div class="abs hang-slot"></div>
  <div class="abs hang-hole"></div>

  <div class="abs logo-box logo-box--front">
    <span class="logo-mark"></span>
    <span class="logo-name">PELLMONT<br>ROOFING &amp; SIDING</span>
  </div>

  <h1 class="abs headline">
    <span class="line">Raised</span>
    <span class="line">On <span class="accent">Care,</span></span>
    <span class="line">Proven Through</span>
    <span class="line">Seasons</span>
  </h1>

  <svg class="abs years-badge" viewBox="0 0 140 140" aria-label="32 years in Calgary">
    <defs><clipPath id="badgeClip"><circle cx="70" cy="70" r="63"/></clipPath></defs>
    <circle cx="70" cy="70" r="69" fill="#5f6266"/>
    <circle cx="70" cy="70" r="66" fill="#fff"/>
    <circle cx="70" cy="70" r="63" fill="var(--blue)"/>
    <text x="72" y="70" text-anchor="middle" font-family="Anton, sans-serif" font-size="56" fill="#fff">32</text>
    <text x="70" y="98" text-anchor="middle" font-family="Anton, sans-serif" font-size="26" fill="#1d2733">YEARS</text>
    <rect x="0" y="101" width="140" height="10" fill="#fff" clip-path="url(#badgeClip)"/>
    <text x="70" y="109.5" text-anchor="middle" font-family="Poppins, sans-serif" font-weight="600" font-size="9" fill="#1d2733">IN CALGARY</text>
  </svg>

  <svg class="abs footer-wave" style="top:540px" width="392" height="417" viewBox="0 540 392 417" preserveAspectRatio="none">
    <path d="M0 637 Q196 561 392 637 L392 957 L0 957 Z" fill="var(--blue)"/>
    <path d="M0 662 Q196 556 392 662 L392 957 L0 957 Z" fill="var(--dark)"/>
  </svg>

  <h2 class="abs about-title">ABOUT US:</h2>
  <p class="abs about-copy">We pride ourselves in providing excellent customer service and quality workmanship. We work with honesty and integrity and staff expert managers, supervisors and tradespeople. We provide satisfaction and ease of mind through our knowledge and experience throughout the duration of the project.</p>

  <div class="abs warranty">
    <svg class="abs warranty-years" viewBox="0 0 132 45">
      <polygon points="0,0 122,0 132,22.5 122,45 0,45" fill="var(--blue)"/>
      <text x="60" y="39" text-anchor="middle" font-family="Anton, sans-serif" font-size="40" fill="#fff">25 YEAR</text>
    </svg>
    <svg class="abs warranty-label" viewBox="0 0 143 45">
      <polygon points="0,0 143,0 143,45 0,45 10,22.5" fill="var(--warranty-grey)"/>
      <text x="78" y="23" text-anchor="middle" font-family="Oswald, sans-serif" font-weight="700" font-size="23" fill="#fff">LABOUR</text>
      <text x="78" y="41" text-anchor="middle" font-family="Oswald, sans-serif" font-weight="700" font-size="15" fill="#fff">WARRANTY'S</text>
    </svg>
    <div class="abs warranty-available">AVAILABLE</div>
  </div>

  <p class="abs offer" style="top:784px">We are in your area, contact us today for your Exclusive limited time offer!</p>
  <div class="abs phone" style="top:800px">
    <span class="phone-icon"><svg width="18" height="18" viewBox="0 0 24 24"><path fill="#fff" d="M6.6 10.8a15.1 15.1 0 0 0 6.6 6.6l2.2-2.2c.3-.3.7-.4 1-.2 1.1.4 2.3.6 3.6.6.6 0 1 .4 1 1V20c0 .6-.4 1-1 1A17 17 0 0 1 3 4c0-.6.4-1 1-1h3.5c.6 0 1 .4 1 1 0 1.3.2 2.5.6 3.6.1.3 0 .7-.2 1z"/></svg></span>
    <span>(403) 555-0148</span>
  </div>
  <p class="abs web" style="top:840px">www.Loreumipsum.com</p>

  <div class="abs badges">
    <span class="badge badge--wide"></span>
    <span class="badge badge--diamond"></span>
    <span class="badge badge--tile"></span>
    <span class="badge badge--plate"></span>
    <span class="badge badge--dot"></span>
  </div>
  <p class="abs disclaimer">*discounts apply exclusively to new agreements only</p>
</section>

<!-- BACK -->
<section class="hanger hanger--back">
  <div class="abs photo-home" role="img" aria-label="Photo of a family sitting on the lawn in front of a grey two-storey home with white porch"></div>
  <div class="abs hang-hole"></div>

  <div class="abs services-pill">SERVICES:</div>

  <div class="abs thumb thumb--roofing" style="left:63px;top:404px" role="img" aria-label="Photo of a home with a new shingle roof"></div>
  <div class="abs thumb thumb--siding" style="left:245px;top:404px" role="img" aria-label="Photo of a house clad in dark siding"></div>
  <div class="abs thumb thumb--cladding" style="left:63px;top:546px" role="img" aria-label="Photo of aluminum cladding around a window"></div>
  <div class="abs thumb thumb--soffit" style="left:245px;top:546px" role="img" aria-label="Photo of soffit, fascia and eavestrough against the sky"></div>

  <div class="abs divider-v"></div>
  <div class="abs divider-h"></div>

  <div class="abs service" style="left:20px;top:472px">
    <h3 class="service-title">ROOFING</h3>
    <p class="service-copy">For re-roofs, new roofs, repairs or inspections, we will be happy to answer all the questions you can send our way.</p>
  </div>
  <div class="abs service" style="left:201px;top:470px">
    <h3 class="service-title">SIDING</h3>
    <p class="service-copy">Proper siding will not only help keep heat in your home, it will help keep the elements along with annoying pests out.</p>
  </div>
  <div class="abs service" style="left:20px;top:612px">
    <h3 class="service-title">CLADDING</h3>
    <p class="service-copy">We offer custom pre-bent aluminum cladding to protect exposed wood products such as window battens and frames, beams, columns, and door frames.</p>
  </div>
  <div class="abs service" style="left:201px;top:612px">
    <h3 class="service-title">SOFFIT &amp; FASCIA</h3>
    <p class="service-copy">No home is complete without proper water drainage to keep your new siding and roof in proper condition.</p>
  </div>

  <svg class="abs footer-wave" style="top:680px" width="392" height="277" viewBox="0 680 392 277" preserveAspectRatio="none">
    <path d="M0 726 Q196 652 392 726 L392 957 L0 957 Z" fill="var(--blue)"/>
    <path d="M0 754 Q196 642 392 754 L392 957 L0 957 Z" fill="var(--dark)"/>
  </svg>

  <div class="abs logo-box logo-box--back">
    <span class="logo-mark"></span>
    <span class="logo-name">PELLMONT<br>ROOFING &amp; SIDING</span>
  </div>

  <p class="abs offer" style="top:783px">We are in your area, contact us today for your Exclusive limited time offer!</p>
  <div class="abs phone" style="top:800px">
    <span class="phone-icon"><svg width="18" height="18" viewBox="0 0 24 24"><path fill="#fff" d="M6.6 10.8a15.1 15.1 0 0 0 6.6 6.6l2.2-2.2c.3-.3.7-.4 1-.2 1.1.4 2.3.6 3.6.6.6 0 1 .4 1 1V20c0 .6-.4 1-1 1A17 17 0 0 1 3 4c0-.6.4-1 1-1h3.5c.6 0 1 .4 1 1 0 1.3.2 2.5.6 3.6.1.3 0 .7-.2 1z"/></svg></span>
    <span>(403) 555-0148</span>
  </div>
  <p class="abs web" style="top:840px">www.Loreumipsum.com</p>

  <div class="abs badges">
    <span class="badge badge--wide"></span>
    <span class="badge badge--diamond"></span>
    <span class="badge badge--tile"></span>
    <span class="badge badge--plate"></span>
    <span class="badge badge--dot"></span>
  </div>
  <p class="abs disclaimer">*discounts apply exclusively to new agreements only</p>
</section>

</body>
</html>
```